YourTidemill Flyer

I require an A5 sized flyer to be designed that advertised the new flexible workspace of YourTidemill.
should say it is a "Flexible Workspace with EV Charging"
web address is www.yourtidemill.co.uk
It should show the 3 different types of membership as priced on the website

```html
<!DOCTYPE html>
<html lang="en">
<head>
<meta charset="utf-8">
<title>YourTidemill Flyer</title>
<link href="https://fonts.googleapis.com/css2?family=Oswald:wght@500;600;700&family=Arimo:wght@400;700&display=swap" rel="stylesheet">
<style>
:root{
  --orange:#f0921e;
  --dark:#3a3a3c;
  --white:#ffffff;
  --bg:#e8e8e8;
  --text:#2b2b2b;
}
*{margin:0;padding:0;box-sizing:border-box}
html,body{width:1200px;height:1200px;overflow:hidden;background:var(--bg)}
body{position:relative;font-family:"Arimo",Arial,sans-serif;color:var(--text)}
.page{position:absolute;top:230px;width:524px;height:740px;background:var(--white);overflow:hidden;box-shadow:0 4px 14px rgba(0,0,0,.18)}
.page--front{left:52px}
.page--back{left:624px}
.brand{position:absolute;top:30px;left:0;width:100%;text-align:center;font-family:"Oswald",sans-serif;font-weight:700;font-size:40px;color:var(--dark);line-height:46px;letter-spacing:.5px}
.brand__dot{display:inline-block;width:12px;height:12px;background:var(--orange);border-radius:50%;margin-right:8px;vertical-align:middle}

/* front */
.hero{position:absolute;left:0;top:122px;width:524px;height:274px;background:#4a4a4c}
.hero__photo{position:absolute;left:0;top:0}
.hero__title{position:absolute;right:21px;top:38px;text-align:right;font-family:"Oswald",sans-serif;font-weight:700;font-style:italic;font-size:44px;line-height:51px;color:var(--white)}
.divider{position:absolute;left:0;top:450px;width:196px;height:12px;background:var(--dark)}
.divider__tip{position:absolute;left:200px;top:450px}
.intro{position:absolute;left:0;top:487px;width:524px;height:163px;background:var(--orange)}
.intro__text{position:absolute;left:22px;top:16px;font-size:14px;line-height:19.4px;color:var(--white);white-space:nowrap}
.lounge-photo{position:absolute;left:191px;top:415px}

/* footer */
.footer{position:absolute;left:0;bottom:0;width:524px;height:50px}
.footer__band{position:absolute;left:0;top:0}
.footer__item{position:absolute;top:0;height:50px;font-size:14.5px;color:var(--white);display:flex;align-items:center;gap:9px;white-space:nowrap}
.footer__item svg{flex:none;display:block}
.footer__item--web{left:22px}
.footer__item--mail{right:22px}

/* back */
.package-title{position:absolute;left:129px;top:122px;width:260px;height:32px}
.package-title__bar{position:absolute;left:15px;top:0;width:231px;height:32px;background:var(--dark);border-radius:4px;border:2px solid var(--white)}
.package-title__cap{position:absolute;top:2px;width:14px;height:28px;background:var(--orange);border-radius:3px}
.package-title__text{position:absolute;left:0;top:0;width:100%;text-align:center;font-family:"Oswald",sans-serif;font-weight:500;font-size:22px;line-height:31px;color:var(--white)}
.tier{position:absolute;left:0;width:524px}
.tier__tab{position:absolute;left:0;top:0;height:30px}
.tier__name{position:absolute;left:56px;top:0;font-family:"Oswald",sans-serif;font-weight:500;font-size:18.5px;line-height:30px;color:var(--white)}
.tier__icon{position:absolute;left:22px;top:3px}
.tier__list{position:absolute;left:24px;list-style:none}
.tier__list li{position:relative;padding-left:9px;font-size:12px;height:20.4px;line-height:20.4px;white-space:nowrap}
.tier__list li::before{content:"";position:absolute;left:-1px;top:8px;width:4px;height:4px;border-radius:50%;background:var(--orange)}
.tier__list small{font-size:10px}
.price{position:absolute;left:341px;width:152px;border:1.5px solid var(--dark);padding:2px}
.price__inner{background:var(--orange);color:var(--white);font-weight:700;text-align:center;font-size:15.5px;line-height:19px;display:flex;align-items:center;justify-content:center;flex-direction:column}
.price__note{position:absolute;left:341px;width:152px;text-align:center;font-size:7.6px;line-height:10px}
.price__tag{position:absolute;left:387px;width:60px;height:10px;background:var(--dark);color:var(--white);border-radius:2px;text-align:center;font-size:7.8px;font-weight:700;line-height:10px}
.cable{position:absolute;left:0;top:0}
</style>
</head>
<body>

<section class="page page--front">
  <div class="brand"><span class="brand__dot"></span>YourTidemill</div>

  <div class="hero">
    <svg class="hero__photo" width="524" height="274" viewBox="0 0 524 274" role="img" aria-label="Open-plan workspace with breakfast bar, high stools and leather sofas">
      <defs><linearGradient id="heroGrad" x1="0" y1="0" x2="1" y2="1"><stop offset="0" stop-color="#b9bcbd"/><stop offset=".55" stop-color="#8d8a85"/><stop offset="1" stop-color="#6b5a4b"/></linearGradient></defs>
      <polygon points="0,26 336,26 280,250 0,250" fill="url(#heroGrad)"/>
      <rect x="0" y="0" width="524" height="26" fill="#5c5c5e"/>
    </svg>
    <div class="hero__title">Flexible<br>Workspace<br>with<br>EV Charging</div>
  </div>

  <div class="divider"></div>
  <svg class="divider__tip" width="14" height="13" viewBox="0 0 14 13"><polygon points="4,0 14,0 10,13 0,13" fill="var(--orange)"/></svg>

  <div class="intro">
    <p class="intro__text">YourTidemill is a unique<br>workspace environment for<br>EV owners looking to<br>recharge their Electric<br>Vehicles, grab a snack and<br>beverage, and catch up<br>with some office work.</p>
  </div>
  <svg class="lounge-photo" width="333" height="223" viewBox="0 0 333 223" role="img" aria-label="Lounge area with brown leather chesterfield sofas, coffee tables and booth seating">
    <defs><linearGradient id="loungeGrad" x1="0" y1="0" x2="0" y2="1"><stop offset="0" stop-color="#c9cacc"/><stop offset=".45" stop-color="#9a958f"/><stop offset="1" stop-color="#6e5443"/></linearGradient></defs>
    <polygon points="56,0 333,0 333,223 0,223" fill="url(#loungeGrad)"/>
  </svg>

  <div class="footer">
    <svg class="footer__band" width="524" height="50" viewBox="0 0 524 50"><rect width="524" height="50" fill="var(--dark)"/><polygon points="0,0 274,0 253,50 0,50" fill="var(--orange)"/></svg>
    <div class="footer__item footer__item--web">
      <svg width="15" height="15" viewBox="0 0 16 16" fill="none" stroke="#fff" stroke-width="1.2"><circle cx="8" cy="8" r="7"/><ellipse cx="8" cy="8" rx="3" ry="7"/><line x1="1" y1="8" x2="15" y2="8"/><line x1="2" y1="4.5" x2="14" y2="4.5"/><line x1="2" y1="11.5" x2="14" y2="11.5"/></svg>
      <span>www.yourtidemill.co.uk</span>
    </div>
    <div class="footer__item footer__item--mail">
      <svg width="15" height="12" viewBox="0 0 16 12" fill="none" stroke="#fff" stroke-width="1.2"><rect x=".6" y=".6" width="14.8" height="10.8"/><polyline points=".6,.6 8,7 15.4,.6"/><line x1=".6" y1="11.4" x2="6" y2="6"/><line x1="15.4" y1="11.4" x2="10" y2="6"/></svg>
      <span>info@yourtidemill.co.uk</span>
    </div>
  </div>
</section>

<section class="page page--back">
  <div class="brand"><span class="brand__dot"></span>YourTidemill</div>

  <div class="package-title">
    <span class="package-title__cap" style="left:0"></span>
    <span class="package-title__cap" style="right:0"></span>
    <div class="package-title__bar"></div>
    <div class="package-title__text">Membership Package</div>
  </div>

  <svg class="cable" width="524" height="560" viewBox="0 0 524 560" fill="none" stroke="var(--orange)" stroke-width="2.2">
    <polyline points="211,183 500,183 500,265 370,265"/>
    <polyline points="211,287 500,287 500,369 370,369"/>
    <polyline points="211,435 500,435 500,515 370,515"/>
    <g fill="var(--orange)" stroke="none">
      <g transform="translate(316,256)"><rect x="0" y="2" width="8" height="3"/><rect x="0" y="13" width="8" height="3"/><rect x="7" y="0" width="14" height="18" rx="2"/><polygon points="21,3 36,7 54,8 54,10 36,11 21,15"/></g>
      <g transform="translate(316,360)"><rect x="0" y="2" width="8" height="3"/><rect x="0" y="13" width="8" height="3"/><rect x="7" y="0" width="14" height="18" rx="2"/><polygon points="21,3 36,7 54,8 54,10 36,11 21,15"/></g>
      <g transform="translate(316,506)"><rect x="0" y="2" width="8" height="3"/><rect x="0" y="13" width="8" height="3"/><rect x="7" y="0" width="14" height="18" rx="2"/><polygon points="21,3 36,7 54,8 54,10 36,11 21,15"/></g>
    </g>
  </svg>

  <div class="tier" style="top:169px">
    <svg class="tier__tab" width="212" height="30" viewBox="0 0 212 30"><polygon points="0,0 199,0 193,30 0,30" fill="var(--dark)"/><polygon points="203,0 212,0 206,30 197,30" fill="var(--orange)"/></svg>
    <svg class="tier__icon" width="26" height="24" viewBox="0 0 26 24" fill="none" stroke="var(--orange)" stroke-width="1.4"><rect x="1" y="6" width="24" height="16" rx="2"/><path d="M9 6V3h8v3"/><line x1="1" y1="13" x2="25" y2="13"/><rect x="11" y="11" width="4" height="4"/></svg>
    <div class="tier__name">Day Member</div>
    <ul class="tier__list" style="top:34px">
      <li>Use of Hot Desks &amp; Lounge Areas</li>
      <li>Secure Wifi</li>
      <li>Free Tea &amp; Coffee</li>
    </ul>
  </div>
  <div class="price" style="top:189px"><div class="price__inner" style="height:39px">£25.00<br>Each Visit</div></div>
  <div class="price__note" style="top:237px">Price Inclusive of VAT</div>
  <div class="price__tag" style="top:248px">Each Visit</div>

  <div class="tier" style="top:273px">
    <svg class="tier__tab" width="212" height="30" viewBox="0 0 212 30"><polygon points="0,0 199,0 193,30 0,30" fill="var(--dark)"/><polygon points="203,0 212,0 206,30 197,30" fill="var(--orange)"/></svg>
    <svg class="tier__icon" width="26" height="24" viewBox="0 0 26 24" fill="none" stroke="var(--orange)" stroke-width="1.4"><circle cx="12" cy="13" r="10"/><circle cx="12" cy="13" r="6"/><circle cx="12" cy="13" r="2"/><line x1="12" y1="13" x2="23" y2="2"/><path d="M20 2h3v3"/></svg>
    <div class="tier__name">Light Member</div>
    <ul class="tier__list" style="top:34px">
      <li>Use of Hot Desks &amp; Lounge Areas</li>
      <li>Secure Wifi</li>
      <li>Free Tea &amp; Coffee</li>
      <li>Discounted E/V Charge Rates</li>
      <li>Access to Meeting Rooms <small>(£10+ vat per person, per hour)</small></li>
    </ul>
  </div>
  <div class="price" style="top:292px"><div class="price__inner" style="height:41px">£18 a month<br>+ £18 Each Visit</div></div>
  <div class="price__note" style="top:341px">Price Inclusive of VAT</div>
  <div class="price__tag" style="top:352px">Per month</div>

  <div class="tier" style="top:419px">
    <svg class="tier__tab" width="212" height="30" viewBox="0 0 212 30"><polygon points="0,0 199,0 193,30 0,30" fill="var(--dark)"/><polygon points="203,0 212,0 206,30 197,30" fill="var(--orange)"/></svg>
    <svg class="tier__icon" width="28" height="24" viewBox="0 0 28 24" fill="none" stroke="var(--orange)" stroke-width="1.4"><polygon points="6,1 22,1 27,8 14,23 1,8"/><line x1="1" y1="8" x2="27" y2="8"/><polyline points="10,1 8,8 14,23 20,8 18,1"/></svg>
    <div class="tier__name">All Access Member</div>
    <ul class="tier__list" style="top:32px">
      <li>Unlimited Number of Visits Each Month</li>
      <li>Dedicated Desk <small>(lockable draws + £60 a month)</small></li>
      <li>Receptionist to Meet &amp; Greet Guests</li>
      <li>Discounted E/V Charge Rates</li>
      <li>Access to Meeting Rooms <small>(£10+vat per person, per hour)</small></li>
      <li>Use of Lounge Areas</li>
      <li>Secure Wifi</li>
      <li>Free Tea &amp; Coffee</li>
      <li>Discounted E/V Charge Rates</li>
      <li>Access to Meeting Rooms <small>(£10+ vat per person, per hour)</small></li>
    </ul>
  </div>
  <div class="price" style="top:439px"><div class="price__inner" style="height:40px">£180.00</div></div>
  <div class="price__note" style="top:488px">Price Inclusive of VAT</div>
  <div class="price__tag" style="top:499px">Per month</div>

  <div class="footer">
    <svg class="footer__band" width="524" height="50" viewBox="0 0 524 50"><rect width="524" height="50" fill="var(--dark)"/><polygon points="0,0 274,0 253,50 0,50" fill="var(--orange)"/></svg>
    <div class="footer__item footer__item--web">
      <svg width="15" height="15" viewBox="0 0 16 16" fill="none" stroke="#fff" stroke-width="1.2"><circle cx="8" cy="8" r="7"/><ellipse cx="8" cy="8" rx="3" ry="7"/><line x1="1" y1="8" x2="15" y2="8"/><line x1="2" y1="4.5" x2="14" y2="4.5"/><line x1="2" y1="11.5" x2="14" y2="11.5"/></svg>
      <span>www.yourtidemill.co.uk</span>
    </div>
    <div class="footer__item footer__item--mail">
      <svg width="15" height="12" viewBox="0 0 16 12" fill="none" stroke="#fff" stroke-width="1.2"><rect x=".6" y=".6" width="14.8" height="10.8"/><polyline points=".6,.6 8,7 15.4,.6"/><line x1=".6" y1="11.4" x2="6" y2="6"/><line x1="15.4" y1="11.4" x2="10" y2="6"/></svg>
      <span>info@yourtidemill.co.uk</span>
    </div>
  </div>
</section>

</body>
</html>
```